Digitales Briefpapier für IT-Systemhaus
Zielgruppe
IT-Systemhaus mit dem Schwerpunkt Digitalisierung von Geschäftsprozessen. Ggf. Schlagwörter wie DMS, ECM, Digitalisierung Ihrer Prozesse unterbringen.
Aufgabenstellung
Digitale Vorlage (Word) um daraus dann ein PDF zu generieren. Anschrift usw. auf QXN.de

```html
<!DOCTYPE html>
<html lang="de">
<head>
<meta charset="utf-8">
<title>QXN.de Briefpapier</title>
<link href="https://fonts.googleapis.com/css2?family=Exo+2:wght@300;500&display=swap" rel="stylesheet">
<style>
  :root {
    --brand-blue: #3262a6;
    --accent-blue: #4a78c2;
    --text-grey: #4a4a4a;
    --rule-grey: #c9c9c9;
    --paper: #ffffff;
  }
  html, body { margin: 0; padding: 0; overflow: hidden; }
  body { width: 847px; height: 1200px; background: var(--paper); }
  .letterhead {
    position: relative; width: 847px; height: 1200px; overflow: hidden;
    background: var(--paper);
    font-family: "Exo 2", sans-serif; font-weight: 300; color: var(--text-grey);
  }
  .header-band {
    position: absolute; left: 0; top: 0; width: 847px; height: 116px;
    background: var(--brand-blue);
  }
  .tagline {
    position: absolute; left: 75px; top: 48px; margin: 0;
    font-size: 13px; font-weight: 500; color: #fff; letter-spacing: 0.1px;
  }
  .company-name {
    position: absolute; right: 78px; top: 36px; margin: 0;
    font-size: 36px; font-weight: 500; color: #fff; letter-spacing: 0; line-height: 1;
  }
  .sender-line {
    position: absolute; left: 123px; top: 180px; margin: 0;
    font-size: 7px; color: #888;
  }
  .sender-line .company { color: var(--accent-blue); }
  .contact-block {
    position: absolute; left: 589px; top: 150px;
    font-size: 12px; line-height: 14.6px; font-style: normal;
  }
  .contact-block p { margin: 0 0 7px; }
  .blue { color: var(--accent-blue); }
  .fold-mark { position: absolute; left: 27px; width: 6px; height: 10px; }
  .fold-mark.first { top: 447px; }
  .fold-mark.second { top: 761px; }
  .footer-rule {
    position: absolute; left: 102px; top: 1099px; width: 652px; height: 1px;
    background: var(--rule-grey);
  }
  .footer-col {
    position: absolute; top: 1111px; font-size: 12px; line-height: 15.5px;
  }
  .footer-col p { margin: 0; }
  .footer-col.company { left: 102px; }
  .footer-col.management { left: 370px; }
  .footer-col.bank { left: 522px; }
  .footer-divider {
    position: absolute; top: 1115px; width: 1px; height: 59px; background: var(--accent-blue);
  }
  .footer-divider.one { left: 339px; }
  .footer-divider.two { left: 496px; }
</style>
</head>
<body>
<main class="letterhead">
  <header class="header-band">
    <p class="tagline">DMS, ECM, Digitalisierung Ihrer Prozesse unterbringen.</p>
    <p class="company-name">QXN.de</p>
  </header>

  <p class="sender-line"><span class="company">QXN.de Systemhaus GmbH &amp; Co. KG</span> &nbsp;•&nbsp; Lindenweg 17a &nbsp;•&nbsp; 31999 Kornfeld</p>

  <address class="contact-block">
    <p><span class="blue">QXN.de Systemhaus GmbH &amp; Co. KG</span><br>Lindenweg 17a<br>31999 Kornfeld</p>
    <p><span class="blue">Tel.</span>&nbsp;&nbsp; +49 (555) 0184720<br><span class="blue">Fax.</span>&nbsp; +49 (555) 01847299<br>info@qxn.de<br>www.qxn.de</p>
  </address>

  <svg class="fold-mark first" viewBox="0 0 6 10" aria-hidden="true"><path d="M0 0 L6 5 L0 10 Z" fill="var(--brand-blue)"/></svg>
  <svg class="fold-mark second" viewBox="0 0 6 10" aria-hidden="true"><path d="M0 0 L6 5 L0 10 Z" fill="var(--brand-blue)"/></svg>

  <footer>
    <div class="footer-rule"></div>
    <div class="footer-col company">
      <p class="blue">QXN.de Systemhaus GmbH &amp; Co. KG</p>
      <p>Lindenweg 17a</p>
      <p>31999 Kornfeld</p>
    </div>
    <div class="footer-divider one"></div>
    <div class="footer-col management">
      <p class="blue">Geschäftsführer</p>
      <p>Jonas Beispiel</p>
      <p>Sitz:&nbsp; Kornfeld</p>
      <p>USt:&nbsp; DE000XXXX</p>
    </div>
    <div class="footer-divider two"></div>
    <div class="footer-col bank">
      <p class="blue">Bankverbindung</p>
      <p>Nordkreis Bank</p>
      <p>Bic: NKBXDE00XXX</p>
      <p>IBAN: DE00 XXX00 0000 XXX 0000 00</p>
    </div>
  </footer>
</main>
</body>
</html>
```